Coverseite für Einladungskarte DIN Lang
Zielgruppe
Die Heilkundliche Gemeinschaft Südwestfalen (www.gbwl-heilkunde.de)
Die ambulante Versorgung
Alle Ärzte, Psychologische Psychotherapeuten sowie Kinder- und Jugendlichenpsychotherapeuten in Nordrhein, die Kassenpatienten behandeln, sind in der Heilkundlichen Gemeinschaft (HG) Südwestfalen zusammengeschlossen, um die ambulante medizinische Versorgung der Bevölkerung sicherzustellen. Zugleich ist die HG Südwestfalen Interessenvertreter ihrer Mitglieder.
Die rund 18 500 Vertragsärzte, Psychologischen Psychotherapeuten, Kinder- und Jugendlichenpsychotherapeuten sowie zur ambulanten Behandlung ermächtigten Krankenhausärzte stellen die Versorgung von 9,5 Millionen Menschen in Nordrhein sicher.
Aufgabenstellung
Einladungskarte "Sommerempfang" - Coverseite
Wir benötigen eine Coverseite DIN Lang (210mm x 100 mm) für die Einladungskarte unseres diesjährigen Sommerempfangs.
Der Sommerempfang wird wie jedes Jahr von zwei Institutionen ausgerichtet - von der Heilkundlichen Gemeinschaft (HG) Südwestfalen und der Medizinerbund Ostmark (mbom).
Aus diesem Grund müssen auch die beiden CI Farben in dem Schriftzug "Sommerempfang" enthalten sein - rot vorderer Teil - grün hinterer Teil.
Zusammengefasst:
Die Farben müssen Verwendung finden:
Rot HG Südwestfalen (c 30 | m 100 | y 90 | k 0)
Grün Medizinerbund Ostmark (c 75 | m 5 | y 100 | k 0)
Die Coverseite kann „moderner“ und abstrakter (Beispiel 2016) als die der vergangenen Anfangsjahren des Sommerempfangs gestaltet werden.
Der Schriftzug „Sommerempfang“ muss auf der Coverseite enthalten sein.
Kann/soll aber neu von der Schriftart her gestaltet werden.
Der Schriftzug Sommerempfang – ist unterteilt in rot und grün
(gemeinsame Veranstaltung | Hausfarben der Ausrichter - s.o.)
Der Schriftzug „am 27. September 2017 im Halle am Lindenhof“ kann frei platziert und gestaltet werden.

```html
<!DOCTYPE html>
<html lang="de">
<head>
<meta charset="utf-8">
<title>Sommerempfang – Einladungskarte Cover</title>
<link rel="stylesheet" href="https://fonts.googleapis.com/css2?family=Roboto:wght@100;300&display=swap">
<style>
  :root {
    --stage: #ececea;
    --paper: #ffffff;
    --host-red: #b51f2e;
    --partner-green: #3fa535;
    --frame-grey: #9a9a9a;
    --label-grey: #8c8c8c;
    --petal-deep: #c8140f;
    --petal-bright: #f0401c;
    --petal-light: #ff6a3a;
  }
  html, body {
    margin: 0;
    width: 1200px;
    height: 1200px;
    overflow: hidden;
    background: var(--stage);
  }
  .invitation-cover {
    position: absolute;
    left: 50px;
    top: 338px;
    width: 1100px;
    height: 524px;
    background: var(--paper);
    overflow: hidden;
    box-shadow: 0 6px 18px rgba(0,0,0,0.12);
    font-family: "Roboto", Arial, sans-serif;
  }
  .petal-visual {
    position: absolute;
    top: 0;
    height: 100%;
  }
  .petal-visual--left { left: 0; width: 340px; }
  .petal-visual--right { right: 0; width: 360px; }
  .title-frame {
    position: absolute;
    left: 300px;
    top: 46px;
    width: 500px;
    height: 432px;
    box-sizing: border-box;
    border: 1.5px solid var(--frame-grey);
    background: var(--paper);
  }
  .event-title {
    margin: 0;
    padding: 34px 0 0 62px;
    font-weight: 100;
    font-size: 100px;
    line-height: 0.96;
    letter-spacing: 0.34em;
    text-transform: uppercase;
  }
  .event-title span { display: block; }
  .event-title .host-part { color: var(--host-red); }
  .event-title .partner-part { color: var(--partner-green); }
  .event-date,
  .event-venue {
    position: absolute;
    margin: 0;
    font-weight: 300;
    font-size: 22px;
    color: var(--label-grey);
    background: var(--paper);
    padding: 0 12px;
    white-space: nowrap;
    line-height: 1;
  }
  .event-date {
    right: -1px;
    top: 150px;
    transform-origin: right top;
    transform: translateX(50%) rotate(-90deg) translateX(0);
  }
  .event-venue {
    left: 110px;
    bottom: -12px;
  }
</style>
</head>
<body>
  <section class="invitation-cover">
    <svg class="petal-visual petal-visual--left" viewBox="0 0 340 524" preserveAspectRatio="none" role="img" aria-label="Rote Mohnblütenblätter, angeschnitten am linken Kartenrand">
      <defs>
        <linearGradient id="petalLeft" x1="0" y1="0" x2="1" y2="1">
          <stop offset="0" stop-color="var(--petal-deep)"/>
          <stop offset="0.55" stop-color="var(--petal-bright)"/>
          <stop offset="1" stop-color="var(--petal-light)"/>
        </linearGradient>
      </defs>
      <path d="M0 0 H340 V330 C300 380 250 420 190 410 C140 400 110 360 60 380 C30 392 10 410 0 420 Z" fill="url(#petalLeft)"/>
    </svg>
    <svg class="petal-visual petal-visual--right" viewBox="0 0 360 524" preserveAspectRatio="none" role="img" aria-label="Rote Mohnblütenblätter, angeschnitten am rechten Kartenrand">
      <defs>
        <linearGradient id="petalRight" x1="0" y1="0" x2="1" y2="1">
          <stop offset="0" stop-color="var(--petal-light)"/>
          <stop offset="0.5" stop-color="var(--petal-bright)"/>
          <stop offset="1" stop-color="var(--petal-deep)"/>
        </linearGradient>
      </defs>
      <path d="M360 0 V524 H20 C30 470 10 420 30 360 C40 300 20 250 60 190 C100 130 160 110 230 90 C290 70 330 30 360 0 Z" fill="url(#petalRight)"/>
    </svg>

    <div class="title-frame">
      <h1 class="event-title">
        <span class="host-part">Som</span>
        <span class="host-part">mer</span>
        <span class="partner-part">emp</span>
        <span class="partner-part">fang</span>
      </h1>
      <p class="event-date">27. September 2017</p>
      <p class="event-venue">im Halle am Lindenhof</p>
    </div>
  </section>
</body>
</html>
```